Torvane Dishwasher A5 double sided mailing June 2015

We would like a design doing for us to promote the range of Torvane professional dishwashers. Template attached to show design sizes & layout requirements. I've uploaded some machine pictures & some sample text, although will leave it to artistic impression to design how much or this & how it is presented.

Target Market(s)

Care Homes for the elderly

Industry/Entity Type

It Professional

Requirements
Must have
• Torvane copyright notice "Torvane images © Copyright Torvane @ Hollis KG [2015].
• Torvane Partner 2015 logo which has been uploaded
Nice to have
• Emphasis the 'rental option, although they can be brought too

```html
<!DOCTYPE html>
<html lang="en">
<head>
<meta charset="utf-8">
<title>Torvane Dishwasher Rental Mailer</title>
<link rel="stylesheet" href="https://fonts.googleapis.com/css2?family=Roboto:ital,wght@0,400;0,700;1,400;1,900&family=Open+Sans:wght@400;600&family=Arimo:ital,wght@0,400;1,700&display=swap">
<style>
  :root {
    --page: #e6e6e6;
    --card: #ffffff;
    --brand-blue: #22409a;
    --brand-red: #e3251f;
    --accent-orange: #f26a12;
    --headline-outline: #4a2208;
    --steel-light: #dfe3e8;
    --steel-mid: #b9c0c8;
    --ink: #1a1a1a;
    --muted: #555555;
  }
  * { box-sizing: border-box; margin: 0; padding: 0; }
  html, body { width: 1200px; height: 900px; overflow: hidden; }
  body { background: var(--page); position: relative; font-family: "Roboto", Arial, sans-serif; }

  /* Reverse side (partly behind) */
  .card-back {
    position: absolute; left: 90px; top: 235px; width: 965px; height: 565px;
    background: var(--card); box-shadow: 0 6px 18px rgba(0,0,0,.25); overflow: hidden;
  }
  .card-back .machine-photo {
    position: absolute; left: 0; top: 0; width: 465px; height: 565px;
    background: linear-gradient(180deg, #f4f5f7 0%, var(--steel-light) 55%, #c9ced4 100%);
  }
  .card-back .red-band {
    position: absolute; left: 0; top: 148px; width: 465px; height: 22px;
    background: var(--brand-red);
  }
  .card-back .dealer-name {
    position: absolute; left: 35px; top: 24px; display: flex; align-items: center; gap: 8px;
    font-family: "Roboto", Arial, sans-serif; font-weight: 700; font-size: 38px; color: var(--brand-red);
  }
  .card-back .dealer-name .mark { width: 20px; height: 20px; background: var(--brand-red); }
  .card-back .copyright {
    position: absolute; left: 92px; bottom: 26px;
    font-family: "Open Sans", Arial, sans-serif; font-style: italic; font-size: 14px; color: var(--muted);
  }
  .card-back .feature-panel {
    position: absolute; left: 465px; top: 330px; right: 0; bottom: 0;
    background: var(--brand-blue); padding: 70px 0 0 95px;
  }
  .card-back .feature-list { list-style: none; color: #fff; font-family: "Open Sans", Arial, sans-serif; font-size: 18px; line-height: 23px; }
  .card-back .feature-list li::before { content: "• "; }

  /* Front side */
  .card-front {
    position: absolute; left: 205px; top: 110px; width: 965px; height: 530px;
    background: var(--card); box-shadow: 0 8px 20px rgba(0,0,0,.3); overflow: hidden;
  }
  .offer-band {
    position: absolute; left: 20px; top: 280px; right: 20px; height: 185px;
    background: var(--brand-blue);
  }
  .offer-panel {
    position: absolute; left: 20px; top: 85px; width: 492px; height: 200px;
    background: var(--brand-blue);
  }
  .hand-photo {
    position: absolute; left: 23px; top: 90px; width: 486px; height: 200px;
    background: linear-gradient(180deg, #e9ecf0 0%, #c7cdd4 55%, var(--brand-blue) 100%);
  }
  .headline {
    position: absolute; left: 60px; top: 92px; width: 440px;
    font-family: "Roboto", Arial, sans-serif; font-weight: 900; font-style: italic;
    font-size: 31px; line-height: 36px; color: var(--accent-orange);
    -webkit-text-stroke: 1px var(--headline-outline);
  }
  .headline span { display: block; }
  .headline .second { text-align: right; padding-right: 5px; }
  .benefit-list {
    position: absolute; left: 30px; top: 297px; list-style: none;
    color: #fff; font-style: italic; font-size: 17.5px; line-height: 25px; letter-spacing: .2px;
  }
  .benefit-list li::before { content: "• "; }
  .benefit-list li:nth-child(2) { padding-left: 2px; }
  .dishwasher-photo {
    position: absolute; left: 685px; top: 262px; width: 220px; height: 192px;
    background: linear-gradient(135deg, #eef0f3 0%, #aeb5bd 100%);
  }
  .response-badge { position: absolute; left: 585px; top: 348px; width: 140px; height: 110px; }
  .response-badge text { font-family: "Roboto", Arial, sans-serif; font-weight: 700; font-size: 14px; fill: #fff; }
  .fine-print {
    position: absolute; left: 0; right: 0; top: 468px; text-align: center;
    font-family: "Arimo", Arial, sans-serif; font-size: 12.5px; line-height: 15px; color: var(--ink);
  }
  .fine-print strong { font-style: italic; }
</style>
</head>
<body>
  <section class="card-back">
    <div class="machine-photo" role="img" aria-label="Torvane professional dishwasher in stainless steel"></div>
    <div class="red-band"></div>
    <div class="dealer-name"><span class="mark"></span>Harrow Electrical</div>
    <div class="feature-panel">
      <ul class="feature-list">
        <li>Two Rack High Capacity</li>
        <li>Easy to use touch screen controls</li>
        <li>Freshwater – Optimum cleaning results</li>
        <li>Built in Water Softener</li>
      </ul>
    </div>
    <p class="copyright">Torvane images © Copyright Torvane @ Hollis KG [2015]</p>
  </section>

  <section class="card-front">
    <div class="offer-band"></div>
    <div class="offer-panel"></div>
    <div class="hand-photo" role="img" aria-label="Hand operating the control panel of a stainless steel dishwasher"></div>
    <h1 class="headline"><span>If you don’t want to buy,</span><span class="second">why not rent ?</span></h1>
    <ul class="benefit-list">
      <li>Rental Includes free installation &amp; breakdown repairs.</li>
      <li>No breakdown repair bills.</li>
      <li>No capital Outlay – Just 3 monthly payment deposit is required.</li>
      <li>Free annual service &amp; preventative maintenance checks.</li>
      <li>Rental is off balance sheet – preserving other credit lines.</li>
      <li>Quick Repair service. Or your money back.</li>
    </ul>
    <div class="dishwasher-photo" role="img" aria-label="Open dishwasher loaded with white plates"></div>
    <svg class="response-badge" viewBox="0 0 140 110" aria-label="Guaranteed next day response">
      <polygon fill="#e3251f" points="138,55 124.1,66.4 128.9,82 109.6,86.1 104,101.8 84.5,97.5 70,109 55.5,97.5 36,101.8 30.4,86.1 11.1,82 15.9,66.4 2,55 15.9,43.6 11.1,28 30.4,23.9 36,8.2 55.5,12.5 70,1 84.5,12.5 104,8.2 109.6,23.9 128.9,28 124.1,43.6"/>
      <text x="70" y="42" text-anchor="middle">Guaranteed</text>
      <text x="70" y="59" text-anchor="middle">next day</text>
      <text x="70" y="76" text-anchor="middle">response</text>
    </svg>
    <p class="fine-print">
      <strong>Fixed term applies.</strong> Rental price shown excludes VAT.&nbsp; 3 month deposit followed by monthly payments by direct debit.<br>
      Contact us for further information or copy of T &amp; C’s.&nbsp; One weeks rental refunded for each day outside our service promise.<br>
      Max refund 4 weeks for each individual repair.
    </p>
  </section>
</body>
</html>
```